Website needed for Entertainment Company [Wordpress & Mobile Site] (Contest)

"Vault Learning" does Acrobatic Educational Shows for schools.
We need a 4-Page Wordpress site, for BOTH Desktop & Mobile
THINGS WE'D LIKE ON THE HOME PAGE
- Book Now buttons
- Panel advertising "Kindness-First Tumbling Tour" with subheading "Educating the Victim, Empowering the Bystander, and Enlightening the Bully" with Photo & 'Read More'
- text somewhere saying "Vault Learning engages children in important topics, by utilising Parkour & Acrobatics to captivate and enthrall todays youngest generation."
- Panel advertising Teachers Resources: "Curriculum based resources for teachers including lesson plans, workbooks, and physical activities for before & after the show." Maybe even some boxes that say a subject that is covered (eg. Mathematics. Science. PD/H/PE.)
- Everything else that you recommend
4 PAGES:
- Home Page
- About Us
- Our Program & Shows
- Teachers Resources Portal
NOTE: Transparent & Source files for logo will be provided soon (recently finished being designed)

```html
<!DOCTYPE html>
<html lang="en">
<head>
<meta charset="utf-8">
<title>Vault Learning — Acrobatic Educational Shows</title>
<link href="https://fonts.googleapis.com/css2?family=Rubik+Dirt&family=Oswald:wght@400;500&family=Roboto:wght@400;500&display=swap" rel="stylesheet">
<style>
:root{
  --orange:#f26522;
  --blue:#1b8fd0;
  --blue-dark:#0b67a6;
  --green:#1a8a3a;
  --lime:#8cc63f;
  --cyan:#29abe2;
  --ink:#1d1d1d;
  --text:#444;
  --slate:#2f3541;
  --cell:#f1f1f1;
  --line:#9fd6f0;
}
*{box-sizing:border-box;margin:0;padding:0}
html,body{width:1200px;height:2951px;overflow:hidden;background:#fff}
body{position:relative;font-family:"Roboto",Arial,sans-serif;color:var(--text)}
.abs{position:absolute}
.display{font-family:"Rubik Dirt","Impact",sans-serif;font-weight:400;font-variant:small-caps}
.btn{position:absolute;display:flex;align-items:center;justify-content:center;color:#fff;font-family:"Oswald",sans-serif;font-weight:500;font-size:14px;text-transform:uppercase;letter-spacing:.5px;border-radius:3px;background:linear-gradient(#2aa3e3,var(--blue-dark));box-shadow:0 2px 3px rgba(0,0,0,.25)}
.btn.red{background:linear-gradient(#f0553a,#c42c17)}
.brand{font-family:"Oswald",sans-serif;font-weight:500;color:var(--orange);display:flex;align-items:center;gap:10px;white-space:nowrap}
.brand .dot{border-radius:50%;background:var(--orange);flex:none}

/* header */
.site-header{left:0;top:0;width:1200px;height:87px;background:#fff;box-shadow:0 2px 6px rgba(0,0,0,.15);z-index:2}
.contact-item{display:flex;align-items:center;gap:8px;font-size:13px;color:var(--blue-dark);top:14px}
.icon{width:22px;height:22px}
.nav a{position:absolute;top:56px;font-family:"Oswald",sans-serif;font-size:14px;color:var(--ink);text-decoration:none;text-transform:uppercase}

/* hero */
.hero{left:0;top:87px;width:1200px;height:474px;background:radial-gradient(ellipse at 60% 10%,#4a4a6a 0,#1a1a22 25%,#000 55%)}
.hero h1{left:144px;top:155px;width:520px;font-size:40px;line-height:54px;color:#fff}

/* about */
.about-title{left:0;width:1200px;top:612px;text-align:center;font-size:40px;color:var(--ink)}
.about-brand{left:0;width:1200px;top:672px;justify-content:center;font-size:40px}
.about-text{left:222px;width:758px;top:778px;text-align:center;font-size:12.5px;line-height:20px}

/* show band */
.show-band{left:0;top:948px;width:1200px;height:254px;background:linear-gradient(90deg,#3c4350,var(--slate) 60%,#2a2f39)}
.show-band .big-name{left:232px;top:82px;font-size:56px;line-height:80px}
.show-title{right:157px;top:978px;text-align:right;font-size:30px;line-height:40px;color:#fff}
.show-sub{right:157px;top:1064px;width:440px;text-align:right;font-size:17px;line-height:27px;color:#e8e8e8}

/* curriculum */
.curr-title{left:0;width:1200px;top:1262px;text-align:center;font-size:40px;color:var(--ink)}
.curr-intro{left:222px;width:758px;top:1330px;text-align:center;font-size:12.5px;line-height:20px}
.grid{left:140px;top:1416px;width:918px;height:616px;display:grid;grid-template-columns:repeat(3,306px);grid-template-rows:repeat(2,308px)}
.cell{position:relative;background:linear-gradient(#fafafa,var(--cell));text-align:center;padding:50px 34px 0}
.cell h3{font-family:"Rubik Dirt",sans-serif;font-weight:400;font-variant:small-caps;font-size:24px;margin-bottom:20px}
.cell p{font-size:12.5px;line-height:20px;color:#555}
.cell .btn{position:relative;margin:24px auto 0;width:102px;height:31px}
.photo{position:relative}
.notch{position:absolute;left:50%;bottom:0;transform:translateX(-50%);width:0;height:0;border-left:16px solid transparent;border-right:16px solid transparent;border-bottom:16px solid #fafafa}
.notch.down{top:0;bottom:auto;border-bottom:0;border-top:16px solid var(--cell)}

/* engage band */
.engage{left:0;top:2119px;width:1200px;height:350px;background:#000}
.engage .photo-area{left:640px;top:0;width:560px;height:350px;background:radial-gradient(ellipse at 55% 55%,#6a3a3e 0,#3a1c20 35%,#0a0a0a 75%)}
.engage-text{left:155px;top:36px;width:500px;font-size:27px;line-height:41px;color:#fff}
.o{color:var(--orange)}.g{color:var(--lime)}.c{color:var(--cyan)}

/* contact */
.contact-title{left:0;width:1200px;top:2520px;text-align:center;font-size:40px;color:var(--ink)}
.map{left:161px;top:2622px;width:327px;height:151px;background:linear-gradient(135deg,#eef0e6,#dfe7d6);border:1px solid #ccc}
.info{left:166px;display:flex;align-items:center;gap:10px;font-size:14px;color:var(--blue-dark)}
.field{position:absolute;left:521px;width:246px;height:45px;border:1px solid var(--line);border-radius:3px;font-size:13px;color:#555;padding:13px 10px}
.field.msg{left:783px;width:246px;height:196px}
.footer{left:0;top:2902px;width:1200px;height:49px;border-top:1px solid #ddd;text-align:center;font-size:11px;line-height:40px;color:#555}
</style>
</head>
<body>

<header class="abs site-header">
  <div class="abs contact-item" style="left:152px">
    <svg class="icon" viewBox="0 0 22 22"><circle cx="11" cy="11" r="10" fill="none" stroke="#f26522" stroke-width="2"/><path d="M7.5 6.5l2 2-1 1.5c.8 1.6 1.9 2.7 3.5 3.5l1.5-1 2 2-1.5 1.5c-3.5-.4-6.6-3.5-7-7z" fill="#f26522"/></svg>
    + 555 210 4477
  </div>
  <div class="abs contact-item" style="left:285px">
    <svg class="icon" viewBox="0 0 22 22"><circle cx="11" cy="11" r="10" fill="none" stroke="#f26522" stroke-width="2"/><rect x="6" y="7.5" width="10" height="7" fill="none" stroke="#f26522" stroke-width="1.6"/><path d="M6 7.5l5 4 5-4" fill="none" stroke="#f26522" stroke-width="1.6"/></svg>
    hello@vaultlearning.net
  </div>
  <div class="abs brand" style="left:490px;top:14px;font-size:34px"><span class="dot" style="width:16px;height:16px"></span>Vault Learning</div>
  <div class="btn" style="left:944px;top:14px;width:101px;height:29px">Book Now</div>
  <nav class="nav">
    <a style="left:179px">Home</a>
    <a style="left:244px">About Us</a>
    <a style="left:332px">Our Program &amp; Shows</a>
    <a style="left:749px">Teachers Resources Portal</a>
    <a style="left:946px">Contact Us</a>
  </nav>
</header>

<section class="abs hero" role="img" aria-label="Aerial acrobats performing on hoops and poles on a dark stage">
  <h1 class="abs display">We do Acrobatic Educational Shows for schools.</h1>
</section>

<section>
  <h2 class="abs display about-title">About</h2>
  <div class="abs brand about-brand"><span class="dot" style="width:18px;height:18px"></span>Vault Learning</div>
  <p class="abs about-text">Lorem ipsum dolor sit amet, consectetuer adipiscing elit, sed diam nonummy nibh euismod tincidunt ut laoreet dolore magna aliquam erat volutpat. Ut wisi enim ad minim veniam, quis nostrud exerci tation ullamcorper suscipit lobortis nisl ut aliquip ex ea commodo consequat. Duis autem vel eum iriure dolor in hendrerit in vulputate velit esse molestie consequat, vel illum dolore eu feugiat nulla facilisis at vero eros et accumsan et iusto odio dignissim qui blandit praesent luptatum zzril delenit augue duis dolore te feugait nulla facilisi.</p>
</section>

<section class="abs show-band">
  <div class="abs brand big-name"><span class="dot" style="width:20px;height:20px"></span>Vault Learning</div>
</section>
<h2 class="abs display show-title">Kindness-First<br>Tumbling Tour</h2>
<p class="abs show-sub">Educating the Victim, Empowering the Bystander, and Enlightening the Bully</p>
<div class="btn red" style="left:832px;top:1137px;width:100px;height:31px">View Photos</div>
<div class="btn" style="left:940px;top:1137px;width:103px;height:31px">Read More</div>

<section>
  <h2 class="abs display curr-title">Curriculum Based Resources</h2>
  <p class="abs curr-intro">Lorem ipsum dolor sit amet, consectetuer adipiscing elit, sed diam nonummy nibh euismod tincidunt ut laoreet dolore magna aliquam erat volutpat.</p>
  <div class="abs grid">
    <div class="photo" role="img" aria-label="Young dancer in a colourful costume doing a backbend on stage" style="background:linear-gradient(160deg,#6a5a8a,#2c3a6a 60%,#3a2a4a)"><span class="notch"></span></div>
    <div class="cell">
      <h3 style="color:var(--green)">Workbooks</h3>
      <p>Lorem ipsum dolor sit amet, consectetuer adipiscing elit, sed diam nonummy nibh euismod tincidunt ut laoreet dolore magna aliquam erat volutpat. Ut wisi enim ad minim veniam</p>
      <div class="btn">Read More</div>
    </div>
    <div class="photo" role="img" aria-label="Aerialist posing inside a hoop against a brick wall" style="background:linear-gradient(160deg,#6a3a22,#3a1e12 55%,#1e0f08)"><span class="notch"></span></div>
    <div class="cell">
      <h3 style="color:var(--orange)">Lesson Plans</h3>
      <p>Lorem ipsum dolor sit amet, consectetuer adipiscing elit, sed diam nonummy nibh euismod tincidunt ut laoreet dolore magna aliquam erat volutpat. Ut wisi enim ad minim veniam</p>
      <div class="btn">Read More</div>
    </div>
    <div class="photo" role="img" aria-label="Hands writing with a pen in an open notebook" style="background:linear-gradient(170deg,#a89880,#8a7a66 55%,#2f6a6a)"><span class="notch down"></span></div>
    <div class="cell">
      <h3 style="color:var(--blue)">Physical Activities</h3>
      <p>Lorem ipsum dolor sit amet, consectetuer adipiscing elit, sed diam nonummy nibh euismod tincidunt ut laoreet dolore magna aliquam erat volutpat. Ut wisi enim ad minim veniam</p>
      <div class="btn">Read More</div>
    </div>
  </div>
</section>

<section class="abs engage">
  <div class="abs photo-area" role="img" aria-label="Troupe of acrobats in red and white costumes forming a human pyramid"></div>
  <p class="abs display engage-text"><span class="o">Vault Learning</span> engages children in important topics, by utilising <span class="g">Parkour and Acrobatics</span> to captivate and <span class="c">enthrall todays youngest generation.</span></p>
  <div class="btn" style="left:163px;top:261px;width:101px;height:31px">Book Now</div>
</section>

<section>
  <h2 class="abs display contact-title">Quick Contact</h2>
  <div class="abs map" role="img" aria-label="Road map showing the office location"></div>
  <div class="abs info" style="top:2784px">
    <svg class="icon" viewBox="0 0 22 22"><circle cx="11" cy="11" r="10" fill="none" stroke="#f26522" stroke-width="2"/><path d="M7.5 6.5l2 2-1 1.5c.8 1.6 1.9 2.7 3.5 3.5l1.5-1 2 2-1.5 1.5c-3.5-.4-6.6-3.5-7-7z" fill="#f26522"/></svg>
    + 555 210 4477
  </div>
  <div class="abs info" style="top:2825px">
    <svg class="icon" viewBox="0 0 22 22"><circle cx="11" cy="11" r="10" fill="none" stroke="#f26522" stroke-width="2"/><rect x="6" y="7.5" width="10" height="7" fill="none" stroke="#f26522" stroke-width="1.6"/><path d="M6 7.5l5 4 5-4" fill="none" stroke="#f26522" stroke-width="1.6"/></svg>
    hello@vaultlearning.net
  </div>
  <div class="field" style="top:2624px">Name</div>
  <div class="field" style="top:2674px">Email</div>
  <div class="field" style="top:2724px">Phone</div>
  <div class="field" style="top:2774px">Choose A Topic</div>
  <div class="field msg" style="top:2624px">Message</div>
  <div class="btn" style="left:519px;top:2834px;width:118px;height:34px;font-size:16px">Submit</div>
</section>

<footer class="abs footer">Copyright 2019 &nbsp;Vault Learning | All Right Reserved.</footer>

</body>
</html>
```